Family Owned General Contracting Business Needs Great E-Flyer Design

We need a one page 8.5"x11" e-flyer type pdf document to use as a marketing and advertising tool. We are a licensed general contractor in Phoenix, Arizona. We target and exclusively work with real estate professionals. The main groups of professionals we target are: real estate investors, real estate agents/property managers, property flippers, commercial and multi family investors, insurance restoration professionals. We are looking for a new e-flyer to specifically market our flooring and custom tile work for showers and kitchen backsplashes. We have been in business for 10+ years, and have an A+ QRT rating. We would like the add to appeal to our target demographic, showcasing some portfolio pictures we have, and have a clean, bright design that's simple and not too busy. We would like to see modern colors used similar to the blue in our logo, and other tones like grays, etc.

I would also like it to include an advertisement for a special price for responding to the ad. The price would be $1.95/sq ft for Installation of ceramic tile up to 20" in size.

We would like it to include our email address, website address, company information, and cell phone to contact. It would be great to incorporate our A+ rating with the Fair Trade Registry also.

Company Name: Bellacorte Estate Works LLC
Website: http://bellacorteestateworks.net/
Email: works@bellacorteestates.com
Cell: (602)555-0174

I've attached some portfolio pictures of past work we've completed to entice customers to contact us.

Target Market(s)

Real Estate Professionals looking for the flooring and custom tile services from a General Contractor. The main groups of professionals we target are real estate agents, real estate investors, property managers, commercial and multi family investors, property flippers, and insurance restoration professionals.

Industry/Entity Type

Flooring

Number of Pages Required

1 page

Font styles to use
Sans Serif

Colors
3277b5

Requirements
Must have
• We would like it to include our email address, website address, company information, and cell phone to contact. It would be great to incorporate our A+ rating with the Fair Trade Registry also. We also must have some of the pictures incorporated into the flyer.
• Company Name: Bellacorte Estate Works LLC
• Website: http://bellacorteestateworks.net/
• Email: works@bellacorteestates.com
• Cell: (602)555-0174
Nice to have
• I would also like it to include an advertisement for a special price for responding to the ad. The price would be $1.75/sq ft for Installation of ceramic tile up to 20" in size. Add in that we will provide free estimates.

```html
<!DOCTYPE html>
<html lang="en">
<head>
<meta charset="utf-8">
<title>Bellacorte Estate Works – Tile Flyer</title>
<link rel="stylesheet" href="https://fonts.googleapis.com/css2?family=Montserrat:wght@600;700&family=Roboto:wght@300;400;500;700&display=swap">
<style>
  :root {
    --brand-blue: #3277b5;
    --ink: #1d1d1f;
    --body-grey: #555a60;
    --pale-grey: #f7f7f7;
    --rule: #d9d9d9;
    --white: #ffffff;
  }
  * { margin: 0; padding: 0; box-sizing: border-box; }
  html, body { width: 878px; height: 1200px; overflow: hidden; background: var(--white); }
  .flyer {
    position: relative; width: 878px; height: 1200px; overflow: hidden;
    background: var(--white); font-family: "Roboto", sans-serif; color: var(--ink);
  }
  .backdrop { position: absolute; inset: 0; }
  .brand-mark {
    position: absolute; left: 36px; top: 44px;
    display: flex; align-items: center; gap: 8px;
    font-weight: 500; font-size: 14px; color: var(--brand-blue);
  }
  .brand-mark .dot { width: 12px; height: 12px; background: var(--brand-blue); }
  .company-title {
    position: absolute; top: 530px; left: 0; width: 878px; text-align: center;
    font-family: "Montserrat", sans-serif; font-weight: 700; font-size: 17px; letter-spacing: 0.3px;
  }
  .company-intro {
    position: absolute; top: 568px; left: 0; width: 878px; text-align: center;
    font-size: 8.8px; font-weight: 300; line-height: 17.6px; color: var(--body-grey); white-space: nowrap;
  }
  .offer { position: absolute; left: 576px; top: 702px; width: 260px; }
  .offer-title {
    font-family: "Montserrat", sans-serif; font-weight: 700; font-size: 17.5px; line-height: 25px;
  }
  .offer-text {
    margin-top: 10px; font-size: 11.2px; font-weight: 300; line-height: 23px; color: var(--body-grey);
    white-space: nowrap;
  }
  .offer-text strong { font-size: 15px; font-weight: 700; color: var(--ink); }
  .estimate-button {
    display: inline-block; margin-top: 14px; padding: 0 8px; height: 27px; line-height: 27px;
    background: var(--brand-blue); color: var(--white); font-size: 10.5px; font-weight: 400;
  }
  .rating {
    margin-top: 16px; display: flex; align-items: center; gap: 8px;
    font-size: 11px; font-weight: 400; color: var(--body-grey);
  }
  .rating .badge { width: 14px; height: 14px; border-radius: 50%; background: var(--brand-blue); }
  .rating strong { font-weight: 700; color: var(--ink); }
  .contact-title {
    position: absolute; top: 963px; left: 0; width: 878px; text-align: center;
    font-family: "Montserrat", sans-serif; font-weight: 700; font-size: 18px;
  }
  .contact-line {
    position: absolute; left: 0; width: 878px; display: flex; justify-content: center; align-items: center; gap: 10px;
    font-size: 13px; color: #3a3d42;
  }
  .contact-phone { top: 1012px; }
  .contact-email { top: 1041px; }
  .contact-web { top: 1070px; }
  .contact-line svg { fill: var(--brand-blue); }
  .footer-rule { position: absolute; top: 1116px; left: 151px; width: 615px; height: 1px; background: var(--rule); }
  .copyright { position: absolute; top: 1152px; left: 0; width: 878px; text-align: center; font-size: 10px; color: var(--ink); }
  .page-code { position: absolute; top: 1153px; left: 834px; font-size: 10px; color: var(--ink); }
</style>
</head>
<body>
<main class="flyer">
  <svg class="backdrop" width="878" height="1200" viewBox="0 0 878 1200">
    <defs>
      <linearGradient id="patioTone" x1="0" y1="0" x2="1" y2="1">
        <stop offset="0" stop-color="#8f8c84"/><stop offset="1" stop-color="#b5b0a6"/>
      </linearGradient>
      <linearGradient id="showerTone" x1="0" y1="0" x2="1" y2="0">
        <stop offset="0" stop-color="#e6d8c8"/><stop offset="0.45" stop-color="#5d5a58"/><stop offset="1" stop-color="#3a3a3c"/>
      </linearGradient>
      <linearGradient id="floorTone" x1="0" y1="0" x2="1" y2="1">
        <stop offset="0" stop-color="#7d7a82"/><stop offset="1" stop-color="#b09c8c"/>
      </linearGradient>
      <linearGradient id="bathTone" x1="0" y1="0" x2="1" y2="1">
        <stop offset="0" stop-color="#cfd6dc"/><stop offset="1" stop-color="#3a3c3f"/>
      </linearGradient>
    </defs>
    <polygon class="accent-corner" points="604,0 878,0 878,258" fill="var(--brand-blue)"/>
    <polygon class="pale-panel" points="464,824 878,396 878,1200" fill="var(--pale-grey)"/>
    <polygon role="img" aria-label="Photo of a travertine paver patio with a stone fountain" points="210,96 306,0 572,0 668,96 438,306" fill="url(#patioTone)"/>
    <polygon role="img" aria-label="Photo of a shower wall with black and silver mosaic tile" points="194,112 422,324 194,534 0,341 0,307" fill="url(#showerTone)"/>
    <polygon role="img" aria-label="Photo of a newly tiled floor in a large room" points="688,112 878,302 878,346 688,534 458,324" fill="url(#floorTone)"/>
    <polygon role="img" aria-label="Photo of a tiled bathroom with a mosaic accent strip" points="0,392 466,824 0,1200" fill="url(#bathTone)"/>
    <polygon class="blue-veil" points="0,432 424,824 0,1192" fill="var(--brand-blue)" opacity="0.86"/>
    <circle class="center-emblem" cx="439" cy="455" r="44" fill="var(--brand-blue)"/>
  </svg>

  <div class="brand-mark"><span class="dot"></span>Bellacorte Estate Works LLC</div>

  <h1 class="company-title">BELLACORTE ESTATE WORKS</h1>
  <p class="company-intro">Started in 2006, Bellacorte Estate Works is a family owned and operated business servicing<br>properties in the greater Phoenix area. Our CEO, Marco Bellacorte, is an accomplished contractor<br>and investor, with over 35 years of experience in real estate.</p>

  <section class="offer">
    <h2 class="offer-title">A SPECIAL PRICE FOR<br>RESPONDING TO THE AD</h2>
    <p class="offer-text">The price would be <strong>$1.95/sq</strong> ft for Installation<br>of ceramic tile <strong>up to 20"</strong> in size.</p>
    <span class="estimate-button">FREE ESTIMATES</span>
    <p class="rating"><span class="badge"></span><span><strong>A+</strong> rating with the Fair Trade Registry</span></p>
  </section>

  <h2 class="contact-title">QUICK CONTACT</h2>
  <div class="contact-line contact-phone">
    <svg width="11" height="11" viewBox="0 0 24 24" aria-hidden="true"><path d="M6.6 10.8a15.1 15.1 0 0 0 6.6 6.6l2.2-2.2c.3-.3.7-.4 1-.2 1.1.4 2.3.6 3.6.6.6 0 1 .4 1 1V20c0 .6-.4 1-1 1A17 17 0 0 1 3 4c0-.6.4-1 1-1h3.5c.6 0 1 .4 1 1 0 1.3.2 2.5.6 3.6.1.3 0 .7-.2 1z"/></svg>
    <span>(602)555-0174</span>
  </div>
  <div class="contact-line contact-email">
    <svg width="14" height="11" viewBox="0 0 24 18" aria-hidden="true"><path d="M0 2.5V16c0 1.1.9 2 2 2h20c1.1 0 2-.9 2-2V2.5l-12 8z"/><path d="M1 0h22l-11 7.5z"/></svg>
    <span>works@bellacorteestates.com</span>
  </div>
  <div class="contact-line contact-web">
    <svg width="12" height="12" viewBox="0 0 24 24" aria-hidden="true"><path d="M12 2a10 10 0 1 0 0 20 10 10 0 0 0 0-20zm0 2c.9 1.1 1.7 2.7 2 5h-4c.3-2.3 1.1-3.9 2-5zM9.8 4.4C9.1 5.7 8.6 7.3 8.4 9H4.6a8 8 0 0 1 5.2-4.6zm4.4 0A8 8 0 0 1 19.4 9h-3.8c-.2-1.7-.7-3.3-1.4-4.6zM4.1 11h4.2v2H4.1a8 8 0 0 1 0-2zm6.2 0h3.4v2h-3.4zm5.4 0h4.2a8 8 0 0 1 0 2h-4.2zM4.6 15h3.8c.2 1.7.7 3.3 1.4 4.6A8 8 0 0 1 4.6 15zm5.4 0h4c-.3 2.3-1.1 3.9-2 5-.9-1.1-1.7-2.7-2-5zm5.6 0h3.8a8 8 0 0 1-5.2 4.6c.7-1.3 1.2-2.9 1.4-4.6z"/></svg>
    <span>http://bellacorteestateworks.net/</span>
  </div>

  <div class="footer-rule"></div>
  <p class="copyright">Copyrights@2016Company Name , All rights reserved</p>
  <span class="page-code">C15</span>
</main>
</body>
</html>
```